Visitenkarten-Design für Rohrreinigungsfirma
Zielgruppe
Wir sind eine Kanal.-Rohrreinigungsfirma und suchen ein hochwertiges Design, unsere Zielgruppe sind Firmenkunden,Hausverwaltungen, Architekten sowie Behörden.
Aufgabenstellung
Das Design sollte Edel aussehen. Es sollten unsere Dienstleistungen mit auf der Visitenkarte stehen (gerne auch Rückseite): grabenlose Kanalsanierung, TV-Kamerainspektion,Dichtheitsprüfung DIN EN 1610, Fräsarbeiten mit Roboter, Fräsarbeiten mit Wasserhöchstdruck 2.500 Bar,Verstopfungsbeseitigung. (Vorderseite sollte enthalten:

```html
<!DOCTYPE html>
<html lang="de">
<head>
<meta charset="utf-8">
<title>Visitenkarte Brehm Rohrtechnik</title>
<link href="https://fonts.googleapis.com/css2?family=Montserrat:wght@400;500;600;700&display=swap" rel="stylesheet">
<style>
  :root {
    --navy: #2c3a52;
    --navy-dark: #25324a;
    --link: #3a4f78;
    --red: #c3202c;
    --white: #ffffff;
    --cream-1: #f3ebe0;
    --cream-2: #e8dbc9;
    --page: #eceae6;
  }
  * { margin: 0; padding: 0; box-sizing: border-box; }
  html, body {
    width: 1200px; height: 1085px; overflow: hidden;
    background: var(--page);
    font-family: "Montserrat", Arial, sans-serif;
  }
  .card {
    position: absolute; left: 90px; top: 211px;
    width: 1020px; height: 662px;
    box-shadow: 0 12px 40px rgba(0,0,0,.18);
    overflow: hidden;
  }
  .top-band { height: 50px; background: var(--navy-dark); }
  .head {
    position: relative; height: 218px;
    background: linear-gradient(100deg, var(--cream-1), var(--cream-2));
  }
  .emergency {
    position: absolute; left: 0; top: 50px;
    width: 438px; height: 119px;
    background: var(--red);
    border-radius: 0 60px 60px 0;
    color: var(--white);
  }
  .emergency-text {
    position: absolute; left: 0; top: 13px; width: 330px;
    text-align: center; line-height: 1.22;
  }
  .emergency-title { font-weight: 700; font-size: 26px; letter-spacing: .5px; }
  .emergency-sub { font-weight: 500; font-size: 24px; }
  .emergency-phone { font-weight: 700; font-size: 26px; }
  .emergency-icon { position: absolute; right: 9px; top: 10px; width: 99px; height: 99px; }
  .brand {
    position: absolute; left: 540px; top: 0; width: 450px; height: 218px;
    display: flex; align-items: center; gap: 20px;
  }
  .brand-mark { flex: none; width: 26px; height: 26px; background: var(--navy); }
  .brand-name {
    font-weight: 700; font-size: 48px; line-height: 1.1;
    color: var(--navy); letter-spacing: .5px;
  }
  .body {
    position: relative; height: 304px; background: var(--navy);
    color: var(--white);
  }
  .contact { position: absolute; left: 60px; top: 26px; }
  .person-name { font-weight: 600; font-size: 32px; letter-spacing: 1px; }
  .person-role { font-size: 23px; font-weight: 400; margin-top: 2px; }
  .phone { display: flex; align-items: center; gap: 16px; font-size: 32px; font-weight: 500; margin-top: 28px; }
  .phone svg { width: 28px; height: 28px; }
  .address { font-size: 31px; line-height: 1.3; margin-top: 24px; }
  .services {
    position: absolute; left: 555px; top: 24px; list-style: none;
    font-size: 21px; font-weight: 500; line-height: 1.25;
  }
  .services li { position: relative; padding-left: 22px; margin-bottom: 12px; }
  .services li::before {
    content: ""; position: absolute; left: 2px; top: 10px;
    width: 7px; height: 7px; border-radius: 50%; background: var(--white);
  }
  .foot {
    height: 90px; display: flex; justify-content: space-between; align-items: center;
    padding: 0 60px;
    background: linear-gradient(100deg, var(--cream-1), var(--cream-2));
    color: var(--link); font-weight: 600; font-size: 29px;
  }
</style>
</head>
<body>
  <article class="card">
    <div class="top-band"></div>
    <header class="head">
      <div class="emergency">
        <div class="emergency-text">
          <div class="emergency-title">24H NOTDIENST</div>
          <div class="emergency-sub">Tag &amp; Nacht</div>
          <div class="emergency-phone">0160 - 482 917 30</div>
        </div>
        <svg class="emergency-icon" viewBox="0 0 100 100" aria-hidden="true">
          <circle cx="50" cy="50" r="49" fill="#ffffff"/>
          <path transform="translate(24 24) scale(2.2)" fill="#2c3a52" d="M6.6 10.8c1.4 2.8 3.8 5.1 6.6 6.6l2.2-2.2c.3-.3.7-.4 1-.2 1.1.4 2.3.6 3.6.6.6 0 1 .4 1 1V20c0 .6-.4 1-1 1C10.6 21 3 13.4 3 4c0-.6.4-1 1-1h3.5c.6 0 1 .4 1 1 0 1.3.2 2.5.6 3.6.1.3 0 .7-.2 1z"/>
        </svg>
      </div>
      <div class="brand">
        <span class="brand-mark"></span>
        <span class="brand-name">Brehm<br>Rohrtechnik</span>
      </div>
    </header>
    <section class="body">
      <div class="contact">
        <div class="person-name">JONAS BREHM</div>
        <div class="person-role">Geschäftsführer</div>
        <div class="phone">
          <svg viewBox="0 0 24 24" aria-hidden="true"><path fill="#ffffff" d="M6.6 10.8c1.4 2.8 3.8 5.1 6.6 6.6l2.2-2.2c.3-.3.7-.4 1-.2 1.1.4 2.3.6 3.6.6.6 0 1 .4 1 1V20c0 .6-.4 1-1 1C10.6 21 3 13.4 3 4c0-.6.4-1 1-1h3.5c.6 0 1 .4 1 1 0 1.3.2 2.5.6 3.6.1.3 0 .7-.2 1z"/></svg>
          <span>07120 - 358 24 61</span>
        </div>
        <div class="address">Lindenweg 14<br>72810 Talbach/Oberried</div>
      </div>
      <ul class="services">
        <li>grabenlose Kanalsanierung</li>
        <li>TV-Kamerainspektion</li>
        <li>Dichtheitsprüfung DIN EN 1610</li>
        <li>Fräsarbeiten mit Roboter</li>
        <li>Fräsarbeiten mit<br>Wasserhöchstdruck 2.500 Bar</li>
        <li>Verstopfungsbeseitigung</li>
      </ul>
    </section>
    <footer class="foot">
      <span>info@brehm-rohrtechnik.de</span>
      <span>www.brehm-rohrtechnik.de</span>
    </footer>
  </article>
</body>
</html>
```